Quelt Vodka bottle label

I need a label designed for a vodka bottle. We are a small, farm based distillery producing hand crafted spirits. I've attached a mock-up of a wrap style label on the bottle we use. Logo is also attached. Would like to see it with some prominence at the top of the label. Thinking of a rock / music theme.

Target Market(s)

Adults of drinking age who enjoy quality spirits

Industry/Entity Type

Alcohol beverage production

Requirements
Must have
• Logo on top with Quelt vodka below. Alcohol details also needed: 750 mL 40% alc/vol
Nice to have
• predominantly a black and white label. Maybe a hit of color: copper, silver. Rock theme: guitar / vinyl album

```html
<!DOCTYPE html>
<html lang="en">
<head>
<meta charset="utf-8">
<title>Quelt Vodka – Bottle Label</title>
<link href="https://fonts.googleapis.com/css2?family=Rye&family=Black+Ops+One&display=swap" rel="stylesheet">
<style>
  :root {
    --page: #ffffff;
    --label-black: #030303;
    --ink-white: #f2f2f2;
    --gold-dark: #a5731c;
    --gold-mid: #c8962f;
    --gold-light: #f6d98a;
  }
  html, body {
    margin: 0;
    padding: 0;
    width: 1200px;
    height: 1200px;
    overflow: hidden;
    background: var(--page);
  }
  .canvas {
    position: relative;
    width: 1200px;
    height: 1200px;
  }
  .label-art {
    position: absolute;
    inset: 0;
  }
  .panel-text {
    position: absolute;
    margin: 0;
    color: var(--ink-white);
    text-align: center;
    line-height: 1.2;
  }
  .product-name {
    left: 149px;
    top: 578px;
    width: 200px;
    font-family: "Rye", serif;
    font-size: 20px;
  }
  .bottle-details {
    left: 770px;
    top: 582px;
    width: 230px;
    font-family: "Black Ops One", sans-serif;
    font-size: 22px;
    letter-spacing: 1px;
  }
  .brand-name {
    position: absolute;
    left: 432px;
    top: 560px;
    width: 280px;
    margin: 0;
    text-align: center;
    font-family: "Rye", serif;
    color: var(--ink-white);
    line-height: 1.1;
  }
  .brand-name .brand-word { display: block; font-size: 42px; }
  .brand-name .brand-sub { display: block; font-size: 18px; letter-spacing: 6px; margin-top: 6px; }
</style>
</head>
<body>
<main class="canvas">
  <svg class="label-art" width="1200" height="1200" viewBox="0 0 1200 1200" aria-hidden="false">
    <defs>
      <linearGradient id="goldSheen" x1="0" y1="0" x2="1" y2="0">
        <stop offset="0" stop-color="var(--gold-mid)"/>
        <stop offset="0.35" stop-color="var(--gold-light)"/>
        <stop offset="0.65" stop-color="var(--gold-mid)"/>
        <stop offset="1" stop-color="var(--gold-dark)"/>
      </linearGradient>
    </defs>

    <!-- label body: band with circular crown -->
    <g class="label-body" fill="var(--label-black)">
      <rect x="74" y="462" width="992" height="289"/>
      <circle cx="571" cy="606" r="184"/>
    </g>

    <!-- gold keyline frame -->
    <path class="gold-frame" fill="none" stroke="url(#goldSheen)" stroke-width="3"
      d="M86 480 H472 A155 155 0 0 1 668 480 H1057 V733 H668 A162 162 0 0 1 472 733 H86 Z"/>

    <!-- emblem ring -->
    <circle class="emblem-ring" cx="572" cy="606" r="132" fill="none" stroke="var(--ink-white)" stroke-width="3"/>

    <!-- flourish dividers -->
    <g class="flourish-dividers" fill="url(#goldSheen)">
      <rect role="img" aria-label="Gold scroll flourish divider" x="110" y="516" width="275" height="12" rx="6" opacity="0.85"/>
      <rect role="img" aria-label="Gold scroll flourish divider" x="743" y="516" width="275" height="12" rx="6" opacity="0.85"/>
      <rect role="img" aria-label="Gold scroll flourish divider" x="110" y="672" width="275" height="12" rx="6" opacity="0.85"/>
      <rect role="img" aria-label="Gold scroll flourish divider" x="743" y="672" width="275" height="12" rx="6" opacity="0.85"/>
    </g>
  </svg>

  <p class="panel-text product-name">Handcrafted<br>Vodka</p>

  <h1 class="brand-name">
    <span class="brand-word">Stonevale</span>
    <span class="brand-sub">DISTILLERY</span>
  </h1>

  <p class="panel-text bottle-details">750 ML<br>40% ALC/VOL</p>
</main>
</body>
</html>
```